Business Cards

Business cards (double-sided) to be handed out to clients and potential clients, with contact details, logo .

Target Market(s)

Small to medium size businesses

Industry/Entity Type

Accountants

Contact Information for Business Card

Brightwater Ledger & Counsel Ltd

Colors

Designer to choose only greyscale colors for use in the design.

Requirements
Must have
• Name, Title, Address, Phone number, Email, Website
Nice to have
• Modern, clean lines, classy
Should not have
• Business cards to be double-sided. Form keeps reverting to single-sided.

```html
<!DOCTYPE html>
<html lang="en">
<head>
<meta charset="utf-8">
<title>Brightwater Ledger &amp; Counsel – Business Cards</title>
<link href="https://fonts.googleapis.com/css2?family=Montserrat:wght@400;500;700&display=swap" rel="stylesheet">
<style>
  :root {
    --ink: #0a0a0a;
    --paper: #ffffff;
    --backdrop: #d9d9d9;
    --text: #111111;
  }
  * { box-sizing: border-box; margin: 0; padding: 0; }
  html, body { width: 1200px; height: 900px; overflow: hidden; }
  body {
    background: var(--backdrop);
    font-family: "Montserrat", sans-serif;
    display: flex;
    flex-direction: column;
    align-items: center;
    justify-content: center;
    gap: 30px;
  }
  .card {
    position: relative;
    width: 700px;
    height: 400px;
    box-shadow: 0 6px 18px rgba(0,0,0,0.25);
    overflow: hidden;
  }
  .card-back {
    background: var(--ink);
    display: flex;
    align-items: center;
    justify-content: center;
  }
  .brand-name {
    font-weight: 500;
    letter-spacing: 0.14em;
    text-transform: uppercase;
    line-height: 1.25;
    text-align: left;
  }
  .card-back .brand-name {
    color: var(--paper);
    font-size: 34px;
  }
  .card-front { background: var(--paper); color: var(--text); }
  .swoosh { position: absolute; inset: 0; width: 100%; height: 100%; }
  .holder {
    position: absolute;
    left: 50px;
    top: 62px;
  }
  .holder-name {
    font-weight: 700;
    font-size: 26px;
    letter-spacing: 0.01em;
  }
  .holder-title {
    font-weight: 400;
    font-size: 18px;
    margin-top: 2px;
  }
  .card-front .brand-name {
    position: absolute;
    right: 44px;
    top: 58px;
    font-size: 19px;
    color: var(--text);
  }
  .contact {
    position: absolute;
    left: 60px;
    top: 178px;
    font-size: 17px;
    line-height: 1.45;
    list-style: none;
  }
  .contact li { display: flex; align-items: center; gap: 12px; }
  .contact svg { width: 20px; height: 20px; flex: none; }
  .contact .address { margin-top: 18px; padding-left: 0; display: block; }
  .website {
    position: absolute;
    right: 40px;
    bottom: 40px;
    color: var(--paper);
    font-size: 17px;
  }
</style>
</head>
<body>
  <section class="card card-back" aria-label="Card back">
    <p class="brand-name">Brightwater<br>Ledger &amp; Counsel</p>
  </section>

  <section class="card card-front" aria-label="Card front">
    <svg class="swoosh" viewBox="0 0 700 400" preserveAspectRatio="none" aria-hidden="true">
      <path d="M0,318 C210,322 360,285 470,220 C570,160 630,122 700,110 L700,400 L0,400 Z" fill="var(--ink)"/>
      <path d="M0,352 C230,348 370,300 500,215" fill="none" stroke="var(--paper)" stroke-width="3"/>
    </svg>

    <div class="holder">
      <h1 class="holder-name">DANIEL HARTLEY</h1>
      <p class="holder-title">Managing Director</p>
    </div>

    <p class="brand-name">Brightwater<br>Ledger &amp; Counsel</p>

    <ul class="contact">
      <li>
        <svg viewBox="0 0 24 24" aria-hidden="true"><path fill="var(--text)" d="M6.6 10.8a15.1 15.1 0 0 0 6.6 6.6l2.2-2.2a1 1 0 0 1 1-.25 11.4 11.4 0 0 0 3.6.57 1 1 0 0 1 1 1V20a1 1 0 0 1-1 1A17 17 0 0 1 3 4a1 1 0 0 1 1-1h3.5a1 1 0 0 1 1 1c0 1.25.2 2.45.57 3.57a1 1 0 0 1-.25 1z"/></svg>
        044-987 654 321
      </li>
      <li>
        <svg viewBox="0 0 24 24" aria-hidden="true"><rect x="2" y="5" width="20" height="14" fill="var(--text)"/><path d="M2 5l10 8 10-8" fill="none" stroke="var(--paper)" stroke-width="1.6"/></svg>
        info@brightwaterledger.com
      </li>
      <li class="address">58, Harbour Row<br>Eastmere, 30714</li>
    </ul>

    <p class="website">www.brightwaterledger.com</p>
  </section>
</body>
</html>
```